new Tavrin Care flyer

Redesign our flyer completely. A copy of our current flyers are attached (which are being combined into 1). Use anything from these that u want.
It's given to patients with a whole lot of flyers from our competitors - so needs to stand out
Essential elements are:
1. Text: $99 CPAP Trial (prominent - this is the main point of the flyer)
- Our all inclusive 4 week CPAP or APAP trial includes everything you need to get started for just $99. Plus we'll refund your trial fee when you're ready to buy your own machine.
2. Text: Proudly Independent! (keep this separate from themain promotion.
- Many CPAP clinics in Victoria are now owned by one or other of the big CPAP manufacturers; while many others only stock one brand. We stock all the leading brands and offer genuinely independent advice and friendly service.
3. Text: Call us for an appointment
- Larkfield (03) 9412 6083 5/418 Dorran Street (suburb and phone prominent)
- Holloway (03) 9263 5540 27b Tamsley Grove (suburb and phone prominent)
- Marden East (03) 9351 2874 2637 Fennick Road (suburb and phone prominent)
4. Our logo - attached
5. small supplier logos grouped together - corvane, talvix, morrow&dunlee - attached
6. images for background / filler - talvix machine, mdh machine - attached, must use at least one of talvix pics

```html
<!DOCTYPE html>
<html lang="en">
<head>
<meta charset="utf-8">
<title>Tavrin Care – $99 CPAP Trial flyer</title>
<link href="https://fonts.googleapis.com/css2?family=Dosis:wght@500;700&family=Questrial&display=swap" rel="stylesheet">
<style>
  :root {
    --green: #7dc242;
    --green-dark: #5e9e2c;
    --charcoal: #3b3b3c;
    --charcoal-deep: #262627;
    --paper: #ffffff;
    --mist: #d9d9d9;
    --ink: #1c1c1c;
    --supplier: #2d3d6b;
    --stage: #1b1b1b;
  }
  * { box-sizing: border-box; margin: 0; padding: 0; }
  html, body { width: 1200px; height: 900px; overflow: hidden; background: var(--stage); }
  body { position: relative; font-family: "Questrial", sans-serif; color: var(--ink); }

  .flyer-page {
    position: absolute; top: 30px; width: 440px; height: 840px;
    background: var(--paper); overflow: hidden;
  }
  .flyer-page--promo { left: 140px; }
  .flyer-page--contact { left: 620px; }
  .page-art { position: absolute; inset: 0; width: 100%; height: 100%; }
  .page-content { position: absolute; inset: 0; }

  /* Promo page */
  .brand-name {
    position: absolute; top: 22px; left: 0; right: 0; text-align: center;
    font-family: "Dosis", sans-serif; font-weight: 700; font-size: 62px;
    letter-spacing: 1px; color: var(--green);
  }
  .trial-headline {
    position: absolute; top: 190px; left: 0; right: 0; text-align: center;
    font-family: "Dosis", sans-serif; font-weight: 500; font-size: 48px; color: var(--paper);
  }
  .trial-headline .trial-product { color: var(--green); font-weight: 700; }
  .trial-copy {
    position: absolute; top: 338px; left: 30px; right: 30px; text-align: center;
    font-size: 12.5px; line-height: 1.45;
  }
  .machine-photo { position: absolute; border-radius: 28px; }
  .machine-photo--promo {
    top: 430px; left: 108px; width: 224px; height: 220px;
    background: linear-gradient(160deg, #6b6b6d, #3a3a3c 60%, #222 100%);
  }
  .independent-title {
    position: absolute; top: 662px; left: 0; right: 0; text-align: center;
    font-family: "Dosis", sans-serif; font-weight: 500; font-size: 31px;
    letter-spacing: 1.5px; color: var(--green);
  }
  .independent-copy {
    position: absolute; top: 716px; left: 14px; right: 14px; text-align: center;
    font-size: 12.5px; line-height: 1.4; color: var(--paper);
  }

  .supplier-row {
    position: absolute; bottom: 10px; left: 18px; right: 18px; height: 40px;
    display: flex; justify-content: space-between; align-items: center;
  }
  .supplier-name {
    font-family: "Questrial", sans-serif; font-size: 14px; color: var(--supplier);
    display: flex; align-items: center; gap: 5px;
  }
  .supplier-mark { width: 8px; height: 8px; border-radius: 50%; background: var(--supplier); }

  /* Contact page */
  .appointment-title {
    position: absolute; top: 14px; left: 0; right: 0; text-align: center;
    font-family: "Questrial", sans-serif; font-size: 30px; color: var(--paper);
  }
  .clinic {
    position: absolute; width: 180px; text-align: center; color: var(--paper);
  }
  .clinic--larkfield { left: 10px; top: 152px; }
  .clinic--holloway { left: 230px; top: 142px; }
  .clinic--marden-east { left: 130px; top: 314px; }
  .clinic-suburb {
    font-family: "Dosis", sans-serif; font-weight: 500; font-size: 28px; line-height: 1.15; color: var(--green);
  }
  .clinic-phone { font-size: 14px; letter-spacing: 2px; margin-top: 8px; }
  .clinic-address { font-size: 14px; margin-top: 14px; }
  .machine-photo--contact {
    top: 500px; left: 40px; width: 360px; height: 210px; border-radius: 34px;
    background: linear-gradient(170deg, #4a4a4d, #1e1e20 55%, #0e0e0f);
  }
</style>
</head>
<body>

<section class="flyer-page flyer-page--promo">
  <svg class="page-art" viewBox="0 0 440 840" aria-hidden="true">
    <defs>
      <radialGradient id="promoWash" cx="50%" cy="12%" r="60%">
        <stop offset="0" stop-color="#ffffff"/>
        <stop offset="1" stop-color="#c9c9c9"/>
      </radialGradient>
      <linearGradient id="promoLower" x1="0" y1="0" x2="0" y2="1">
        <stop offset="0" stop-color="#ffffff"/>
        <stop offset="1" stop-color="#e2e2e2"/>
      </linearGradient>
    </defs>
    <rect width="440" height="150" fill="url(#promoWash)"/>
    <rect y="320" width="440" height="520" fill="url(#promoLower)"/>
    <path d="M0,142 Q220,82 440,108 L440,302 Q220,352 0,322 Z" fill="#3b3b3c"/>
    <path d="M0,142 Q220,82 440,108" fill="none" stroke="#7dc242" stroke-width="8"/>
    <path d="M0,156 Q220,98 440,124" fill="none" stroke="#262627" stroke-width="6"/>
    <path d="M0,310 Q220,340 440,290" fill="none" stroke="#262627" stroke-width="6"/>
    <path d="M0,322 Q220,352 440,302" fill="none" stroke="#7dc242" stroke-width="8"/>
    <path d="M0,650 L58,706 L382,706 L440,650 L440,792 L0,792 Z" fill="#7dc242"/>
    <rect y="792" width="440" height="48" fill="#ffffff"/>
    <rect y="834" width="440" height="6" fill="#7dc242"/>
  </svg>
  <div class="page-content">
    <h1 class="brand-name">TAVRIN CARE</h1>
    <h2 class="trial-headline">$99 <span class="trial-product">CPAP</span> Trial</h2>
    <p class="trial-copy">Our all inclusive 4 week CPAP or APAP trial includes everything you need to get started for just $99. Plus we'll refund your trial fee when you're ready to buy your own machine</p>
    <div class="machine-photo machine-photo--promo" role="img" aria-label="Photo of a morrow&amp;dunlee CPAP machine with screen and dial"></div>
    <h2 class="independent-title">Proudly Independent!</h2>
    <p class="independent-copy">Many CPAP clinics in Victoria are now owned by one or other of the big CPAP manufacturers, while many others only stock one brand. We stock all the leading brands and offer genuinely independent advice and friendly service.</p>
    <div class="supplier-row">
      <span class="supplier-name"><span class="supplier-mark"></span>corvane</span>
      <span class="supplier-name"><span class="supplier-mark"></span>talvix</span>
      <span class="supplier-name"><span class="supplier-mark"></span>morrow&amp;dunlee</span>
    </div>
  </div>
</section>

<section class="flyer-page flyer-page--contact">
  <svg class="page-art" viewBox="0 0 440 840" aria-hidden="true">
    <defs>
      <linearGradient id="contactWash" x1="0" y1="0" x2="0" y2="1">
        <stop offset="0" stop-color="#cfcfcf"/>
        <stop offset="0.5" stop-color="#ffffff"/>
        <stop offset="1" stop-color="#e4e4e4"/>
      </linearGradient>
      <radialGradient id="clinicFill" cx="50%" cy="35%" r="65%">
        <stop offset="0" stop-color="#4a4a4b"/>
        <stop offset="1" stop-color="#2a2a2b"/>
      </radialGradient>
    </defs>
    <rect width="440" height="840" fill="url(#contactWash)"/>
    <path d="M0,0 H440 V250 Q220,330 0,260 Z" fill="#3b3b3c"/>
    <g>
      <circle cx="100" cy="200" r="98" fill="#7dc242"/>
      <circle cx="100" cy="200" r="88" fill="#262627"/>
      <circle cx="100" cy="200" r="84" fill="url(#clinicFill)"/>
    </g>
    <g>
      <circle cx="320" cy="190" r="98" fill="#7dc242"/>
      <circle cx="320" cy="190" r="88" fill="#262627"/>
      <circle cx="320" cy="190" r="84" fill="url(#clinicFill)"/>
    </g>
    <g>
      <circle cx="220" cy="362" r="98" fill="#7dc242"/>
      <circle cx="220" cy="362" r="88" fill="#262627"/>
      <circle cx="220" cy="362" r="84" fill="url(#clinicFill)"/>
    </g>
    <path d="M0,738 Q220,700 440,740 L440,790 L0,790 Z" fill="#3b3b3c"/>
    <path d="M0,738 Q220,700 440,740" fill="none" stroke="#7dc242" stroke-width="9"/>
    <path d="M0,770 Q220,740 440,772" fill="none" stroke="#7dc242" stroke-width="5"/>
    <rect y="790" width="440" height="50" fill="#ffffff"/>
  </svg>
  <div class="page-content">
    <h2 class="appointment-title">Call us for an appointment</h2>
    <div class="clinic clinic--larkfield">
      <h3 class="clinic-suburb">Larkfield</h3>
      <p class="clinic-phone">(03) 9412 6083</p>
      <p class="clinic-address">5/418 Dorran Street</p>
    </div>
    <div class="clinic clinic--holloway">
      <h3 class="clinic-suburb">Holloway</h3>
      <p class="clinic-phone">(03) 9263 5540</p>
      <p class="clinic-address">27b Tamsley Grove</p>
    </div>
    <div class="clinic clinic--marden-east">
      <h3 class="clinic-suburb">Marden East</h3>
      <p class="clinic-phone">(03) 9351 2874</p>
      <p class="clinic-address">2637 Fennick Road</p>
    </div>
    <div class="machine-photo machine-photo--contact" role="img" aria-label="Photo of a black talvix CPAP machine with colour touch screen"></div>
    <div class="supplier-row">
      <span class="supplier-name"><span class="supplier-mark"></span>corvane</span>
      <span class="supplier-name"><span class="supplier-mark"></span>talvix</span>
      <span class="supplier-name"><span class="supplier-mark"></span>morrow&amp;dunlee</span>
    </div>
  </div>
</section>

</body>
</html>
```